I need a Professional Eye-Catching Paperback and e-Book Cover Design done with different mockups

I need a Professional Eye-Catching e-Book Cover Design done with different mockups

I need 2-3 designs to choose from per designer.

Book title - Harbor Ledger:

Subtitle - Growing riches that stay behind you

Author name - K. Dapo Renke

I have attached some sample designs but i need you to be creative.

```html
<!DOCTYPE html>
<html lang="en">
<head>
<meta charset="utf-8">
<title>Harbor Ledger — Book Cover</title>
<link href="https://fonts.googleapis.com/css2?family=Barlow+Condensed:wght@600;700&family=Crimson+Text&display=swap" rel="stylesheet">
<style>
  :root {
    --page: #ffffff;
    --cover: #ffffff;
    --ink: #000000;
    --paper: #ffffff;
    --cash-green: #9aa694;
    --cash-light: #d9ddd2;
    --bag-brown: #b9783f;
    --bag-dark: #9c5f2c;
    --edge: #e6e6e6;
  }
  html, body {
    margin: 0;
    padding: 0;
    width: 1050px;
    height: 1200px;
    overflow: hidden;
    background: var(--page);
  }
  .book-cover {
    position: absolute;
    left: 197px;
    top: 137px;
    width: 681px;
    height: 925px;
    background: var(--cover);
    border: 1px solid var(--edge);
    box-sizing: border-box;
    overflow: hidden;
  }
  .title-band {
    position: absolute;
    left: 0;
    top: 80px;
    width: 617px;
    height: 164px;
    background: var(--ink);
  }
  .title-top {
    position: absolute;
    left: 88px;
    top: 72px;
    margin: 0;
    font-family: "Barlow Condensed", sans-serif;
    font-weight: 700;
    font-size: 152px;
    line-height: 1;
    letter-spacing: 6px;
    color: var(--paper);
  }
  .art-upper {
    position: absolute;
    left: 93px;
    top: 244px;
    width: 493px;
    height: 89px;
    background: linear-gradient(180deg, var(--cash-light) 0%, var(--cash-green) 40%, var(--bag-brown) 70%, var(--bag-dark) 100%);
  }
  .title-bottom {
    position: absolute;
    left: 0;
    width: 100%;
    top: 332px;
    margin: 0;
    text-align: center;
    font-family: "Barlow Condensed", sans-serif;
    font-weight: 700;
    font-size: 130px;
    line-height: 1;
    letter-spacing: 6px;
    color: var(--ink);
  }
  .art-lower {
    position: absolute;
    left: 93px;
    top: 446px;
    width: 493px;
    height: 246px;
    background:
      radial-gradient(ellipse 55% 60% at 50% 35%, var(--cash-green) 0%, rgba(154,166,148,0.6) 50%, rgba(255,255,255,0) 100%),
      linear-gradient(180deg, var(--bag-brown) 0%, rgba(185,120,63,0.35) 30%, rgba(255,255,255,0) 70%);
  }
  .subtitle {
    position: absolute;
    left: 0;
    width: 100%;
    top: 730px;
    margin: 0;
    text-align: center;
    padding-left: 30px;
    box-sizing: border-box;
    font-family: "Barlow Condensed", sans-serif;
    font-weight: 600;
    font-size: 27px;
    letter-spacing: 4.2px;
    text-transform: uppercase;
    color: var(--ink);
  }
  .author {
    position: absolute;
    left: 0;
    width: 100%;
    top: 815px;
    margin: 0;
    text-align: center;
    font-family: "Crimson Text", serif;
    font-size: 27px;
    letter-spacing: 2.5px;
    color: var(--ink);
  }
</style>
</head>
<body>
  <main class="book-cover">
    <div class="title-band"></div>
    <h1 class="title-top">HARBOR</h1>
    <div class="art-upper" role="img" aria-label="Stacks of banknotes spilling from the top of an open brown money sack"></div>
    <h2 class="title-bottom">LEDGER</h2>
    <div class="art-lower" role="img" aria-label="Brown money sack tipped open with banknotes falling out below"></div>
    <p class="subtitle">Growing riches that stay behind you</p>
    <p class="author">Author - K. Dapo Renke</p>
  </main>
</body>
</html>
```